依頼詳細
会社の名刺デザインを新しくします。
中核になる3つの事業にそれぞれスタッフがいますが、名刺は共通のものを使用したいと考えています。
スタイリッシュかつ遊び心があって、もらった人が目を引くような名刺にしたいです。
あえてカラーなど希望イメージの指定は致しませんので、多種多様のデザインを見て決めたいと思います。
会社ロゴを添付します。カラーは自由に変更していただいて構いません。
記載項目
表面:社名、事業名、肩書き、名前、連絡先(住所、TEL、FAX、メール等)
裏面:事業内容、プロフィールなど
希望イメージ
シンプル 複雑
単色 カラフル
暗い 明るい
日常 高級
遊び心 厳粛
未来的 伝統的
女性的 男性的
希望する色
設定なし
納品ファイル
設定なし
補足説明
設定なし
縦型、横型、二つ折り名刺、顔写真入りなども特に定めませんので、自由にご提案いただけると選びがいがあり有り難いです。
当選報酬の金額引き上げと選定確約について変更致しました。
よろしくお願い致します。
会社ロゴを添付しました。
ランサーの皆様、たくさんの提案ありがとうございます。
様々な提案を見た結果イメージが固まってきましたので、締め切りを延長して修正等をしていただけないかと思います。

【追記内容】
・事業所名が和風なので、和風な感じが合いそう。
・事業所名の「楓庵の里」は筆文字にしたらいいのではないか?
・匠な感じが出るといい。(白と黒を基調にするとどうなるでしょう?他の色でも構えいません。)
■ 選んだ理由

社員全員による投票にて決定いたしましたので、万人受けしやすいデザインだったのではないかと思います。また、修正等に幾度も迅速に対応していただいた点もよかったです。

■ 提案者全員のお礼・コメント

70を超すランサーの方々から100を超える提案を頂き誠にありがとうございました。当選作品以外にも素晴らしいデザインが多く、選定するのも大変でした。ありがとうございました。

```html
<!DOCTYPE html>
<html lang="ja">
<head>
<meta charset="utf-8">
<title>名刺デザイン 楓庵の里</title>
<link rel="stylesheet" href="https://fonts.googleapis.com/css2?family=Noto+Sans+JP:wght@400;500;700&family=Noto+Serif+JP:wght@400;600&display=swap">
<style>
  :root {
    --cyan: #1ea9cc;
    --cyan-deep: #1596b8;
    --sky: #dff2f8;
    --ink: #333638;
    --rule: #d8dde0;
    --paper: #ffffff;
  }
  * { margin: 0; padding: 0; box-sizing: border-box; }
  html, body { width: 838px; height: 1200px; overflow: hidden; background: var(--paper); }
  body { position: relative; font-family: "Noto Sans JP", sans-serif; color: var(--ink); }

  .card { position: absolute; left: 10px; width: 818px; border: 1px solid var(--rule); background: var(--paper); overflow: hidden; }
  .card--front { top: 12px; height: 556px; }
  .card--back { top: 600px; height: 588px; }

  /* front */
  .office { position: absolute; left: 44px; top: 98px; width: 480px; padding-left: 12px; border-left: 10px solid var(--cyan); }
  .office__name { font-size: 26px; font-weight: 500; letter-spacing: 0.3px; line-height: 1.3; white-space: nowrap; }
  .office__title { font-size: 20px; font-weight: 500; margin-top: 4px; }
  .person { display: flex; align-items: baseline; gap: 16px; margin-top: 2px; }
  .person__name { font-size: 60px; font-weight: 700; color: var(--cyan); letter-spacing: 4px; line-height: 1.15; white-space: nowrap; }
  .person__roman { font-size: 18px; font-weight: 500; color: var(--cyan); white-space: nowrap; }

  .brand { position: absolute; left: 548px; top: 26px; width: 250px; height: 250px; border-radius: 50%; background: var(--cyan); display: flex; align-items: center; justify-content: center; }
  .brand__name { font-family: "Noto Sans JP", sans-serif; font-weight: 700; font-size: 30px; color: var(--paper); letter-spacing: 0.5px; white-space: nowrap; }

  .company { position: absolute; left: 50px; top: 370px; }
  .company__name { font-size: 25px; font-weight: 500; margin-bottom: 12px; }
  .company__line { font-size: 17px; line-height: 1.65; }
  .company__line span { margin-right: 14px; }

  /* back */
  .back__wash { position: absolute; left: 0; top: 0; width: 100%; height: 70px; background: linear-gradient(to bottom, var(--sky), rgba(223,242,248,0)); }
  .back__mark { position: absolute; right: 60px; top: -60px; width: 240px; height: 240px; border-radius: 50%; background: var(--cyan); opacity: 0.08; }
  .profile { position: absolute; left: 0; top: 52px; width: 100%; text-align: center; font-family: "Noto Serif JP", serif; }
  .profile__head { font-family: "Noto Sans JP", sans-serif; font-weight: 700; color: var(--cyan-deep); font-size: 21px; line-height: 1.75; margin-top: 6px; }
  .profile__line { font-size: 19px; line-height: 1.72; }
  .profile__line--tight { font-size: 15.5px; letter-spacing: -0.2px; }
</style>
</head>
<body>
  <section class="card card--front">
    <div class="office">
      <p class="office__name">「居宅介護支援センター楓庵の里」</p>
      <p class="office__title">代表取締役</p>
      <div class="person">
        <span class="person__name">中村 和樹</span>
        <span class="person__roman">Nakamura Kazuki</span>
      </div>
    </div>

    <div class="brand"><span class="brand__name">care harmony</span></div>

    <div class="company">
      <p class="company__name">株式会社 ケアハーモニー</p>
      <p class="company__line">〒890-0000 鹿児島県南浜郡緑町1丁目2-3</p>
      <p class="company__line"><span>tel.0990-12-3456</span><span>fax.0990-12-3457</span><span>e-mail:kazuki@care-harmony.jp</span></p>
    </div>
  </section>

  <section class="card card--back">
    <div class="back__wash"></div>
    <div class="back__mark"></div>
    <div class="profile">
      <p class="profile__head">◆事業内容◆</p>
      <p class="profile__line">介護予防通所介護(介護保険)、通所介護(介護保険)、宿泊サービス(自主事業)</p>
      <p class="profile__head">【理念】</p>
      <p class="profile__line">「よりよい介護で、よりよい生活を Better Life,Better Care」</p>
      <p class="profile__head">【よい介護の条件】</p>
      <p class="profile__line">「本人の意志が尊重され、本人が納得している」</p>
      <p class="profile__line">「QOLの向上に繋がっている」</p>
      <p class="profile__line">「必要に応じ、専門職の意見・サービスを受けることができる」</p>
      <p class="profile__head">【行動指針】</p>
      <p class="profile__line profile__line--tight">「介護をする人、介護を必要とする人にとってどのような状態が一番幸福なのかを考え行動します」</p>
      <p class="profile__line">「よりクオリティの高い介護サービスを提供するため成長し続けます」</p>
      <p class="profile__line">「対立をせずコンセンサスを得ます」</p>
      <p class="profile__line">「個の能力を活かし社会のニーズと結びつけます」</p>
    </div>
  </section>
</body>
</html>
```